Design some Business Cards for my company "Dunecrest Printworks"

Hello Freelancers,

My company needs a business card design. I want it to be unique, elegant and creative. The main colours will be red, white and black.
We only need one side. We recommend you to look at our website before creating a design, here is our website: www.dunecrestprintworks.example

and here is the address:

Dunecrest Printworks
info@dunecrestprintworks.example
+372 813 27460
PO Box 584027-3196
Al Warqaan, Dubai
United Arab Emirates

Thanks very much and good luck

```html
<!DOCTYPE html>
<html lang="en">
<head>
<meta charset="utf-8">
<title>Dunecrest Printworks — Business Card</title>
<link rel="stylesheet" href="https://fonts.googleapis.com/css2?family=Arimo:wght@400;700&display=swap">
<style>
  :root {
    --backdrop: #e9e9e9;
    --card-red-light: #e0202a;
    --card-red-deep: #a30d14;
    --panel-black: #111111;
    --panel-white: #ffffff;
    --text-light: #ffffff;
    --text-dark: #2a0a0b;
  }
  html, body {
    margin: 0;
    width: 1200px;
    height: 901px;
    overflow: hidden;
    background: var(--backdrop);
  }
  .stage {
    width: 1200px;
    height: 901px;
    display: flex;
    align-items: center;
    justify-content: center;
  }
  .business-card {
    width: 900px;
    height: 520px;
    display: block;
    box-shadow: 0 18px 40px rgba(0,0,0,0.18);
  }
  .brand-name {
    font-family: "Arimo", Arial, sans-serif;
    font-weight: 400;
    font-size: 34px;
    fill: var(--text-light);
    letter-spacing: 0.5px;
  }
  .holder-name {
    font-family: "Arimo", Arial, sans-serif;
    font-weight: 700;
    font-size: 26px;
    fill: var(--text-dark);
  }
  .holder-role {
    font-family: "Arimo", Arial, sans-serif;
    font-weight: 400;
    font-size: 22px;
    fill: var(--text-dark);
  }
  .contact-line {
    font-family: "Arimo", Arial, sans-serif;
    font-weight: 400;
    font-size: 22px;
    fill: var(--text-light);
  }
</style>
</head>
<body>
<main class="stage">
  <svg class="business-card" viewBox="0 0 900 520" xmlns="http://www.w3.org/2000/svg" aria-label="Dunecrest Printworks business card">
    <defs>
      <radialGradient id="card-red" cx="62%" cy="45%" r="70%">
        <stop offset="0%" stop-color="var(--card-red-light)"/>
        <stop offset="100%" stop-color="var(--card-red-deep)"/>
      </radialGradient>
    </defs>

    <rect class="card-base" width="900" height="520" fill="url(#card-red)"/>
    <polygon class="corner-black" points="0,0 330,0 0,260" fill="var(--panel-black)"/>
    <polygon class="diagonal-panel" points="0,260 330,0 470,0 420,400 0,330" fill="var(--panel-white)"/>

    <text class="brand-name" x="505" y="150">Dunecrest Printworks</text>

    <text class="holder-name" x="505" y="215">Tariq Haddad</text>
    <text class="holder-role" x="505" y="247">Managing Director</text>

    <text class="contact-line" x="505" y="305">PO Box 584027-3196</text>
    <text class="contact-line" x="505" y="337">Al Warqaan, Dubai</text>
    <text class="contact-line" x="505" y="369">United Arab Emirates</text>
    <text class="contact-line" x="505" y="401">+372 813 27460</text>
    <text class="contact-line" x="505" y="433">info@dunecrestprintworks.example</text>
  </svg>
</main>
</body>
</html>
```